HIgh-end jewelry designer needs a business card design

I need a business card design for the ecclectic & rather expensive jewelry designs. My approach to my work is to combine very old jewelry offset with contemporary items. I enjoy the idea of legacy as well as repurposing finely crafted items that are not possible to create any longer. My desire is to celebrate the past in a contemporary & funky way. The name of my business is VELLORINE. I see my business card design as simple & yet enigmatic as possible. In the end... clean, simple & understated is the look I am after. Thank you for your consideration...

Target Market(s)

I will use this business card for the trade as well as customers

Industry/Entity Type

Business

Contact Information for Business Card

Marta Quorrin Owner/Designer 555-203-7718

Requirements
Must have
• Clean & simple sophisticated design using the word "Vellorinne" as the logo. I like the idea of a play on the word itself, perhaps even using different fonts (i.e.: a bold helvetica combined with a lovely script). I'm afraid to say more because I don't want to limit creative input. Gosh, sometimes it's ok to break the rules!
Nice to have
• In my mind, I have imagined this business card to be simple, using my company name "Vellorine" in a playful yet sophisticated manner. I believe that doing something beautifully simple can be a true challenge. I have imagined something with just black & white, however I am open to ideas... after all that's why I'm here!
Should not have
• As Mozart once said... "It has too many notes!" I know I'm being silly, but I don't want it to be complicated or overly ornate.

```html
<!DOCTYPE html>
<html lang="en">
<head>
<meta charset="utf-8">
<title>Vellorine Business Card</title>
<link rel="stylesheet" href="https://fonts.googleapis.com/css2?family=Pinyon+Script&family=Arimo:ital@0;1&display=swap">
<style>
  :root {
    --backdrop: #2b2a29;
    --card: #0b0b0b;
    --card-edge: #161616;
    --band: rgba(40, 40, 40, 0.88);
    --ink: #ffffff;
    --ink-muted: #707070;
    --jewel-light: #3a3a3a;
    --jewel-mid: #262626;
  }
  html, body {
    margin: 0;
    padding: 0;
    width: 1200px;
    height: 836px;
    overflow: hidden;
    background: var(--backdrop);
  }
  .canvas {
    position: relative;
    width: 1200px;
    height: 836px;
  }
  .card {
    position: absolute;
    left: 100px;
    top: 124px;
    width: 1000px;
    height: 588px;
    background: linear-gradient(180deg, var(--card-edge) 0%, var(--card) 100%);
    overflow: hidden;
    box-shadow: 0 6px 24px rgba(0, 0, 0, 0.45);
  }
  .card__jewelry {
    position: absolute;
    left: 70px;
    top: 0;
    width: 900px;
    height: 588px;
    background:
      radial-gradient(ellipse 26% 40% at 22% 58%, var(--jewel-light) 0%, rgba(38,38,38,0.5) 55%, rgba(11,11,11,0) 100%),
      radial-gradient(ellipse 22% 30% at 45% 42%, var(--jewel-light) 0%, rgba(38,38,38,0.4) 60%, rgba(11,11,11,0) 100%),
      radial-gradient(ellipse 20% 28% at 68% 30%, var(--jewel-mid) 0%, rgba(11,11,11,0) 100%),
      radial-gradient(ellipse 14% 22% at 90% 22%, var(--jewel-mid) 0%, rgba(11,11,11,0) 100%);
  }
  .card__logo {
    position: absolute;
    left: 118px;
    top: 78px;
    margin: 0;
    font-family: "Pinyon Script", cursive;
    font-weight: 400;
    font-size: 112px;
    line-height: 1;
    color: var(--ink);
  }
  .card__band {
    position: absolute;
    left: 380px;
    top: 332px;
    width: 620px;
    height: 104px;
    background: var(--band);
  }
  .card__details {
    position: absolute;
    right: 52px;
    top: 341px;
    text-align: right;
    font-family: "Arimo", Arial, sans-serif;
  }
  .card__name {
    margin: 0;
    font-size: 33px;
    line-height: 44px;
    color: var(--ink);
  }
  .card__role {
    margin: 0;
    font-size: 24px;
    line-height: 34px;
    font-style: italic;
    color: var(--ink-muted);
  }
  .card__contact {
    margin: 32px 0 0;
    font-size: 29px;
    line-height: 40px;
    color: var(--ink);
  }
</style>
</head>
<body>
  <main class="canvas">
    <section class="card">
      <div class="card__jewelry" role="img" aria-label="Faint dark photograph of antique coin jewelry and a beaded necklace"></div>
      <h1 class="card__logo">Vellorine</h1>
      <div class="card__band"></div>
      <div class="card__details">
        <p class="card__name">Marta Quorrin</p>
        <p class="card__role">Jewelry Designer</p>
        <p class="card__contact">555-203-7718 | studio@vellorine.com</p>
      </div>
    </section>
  </main>
</body>
</html>
```